KPT Building And Maintenance

Need a very professional looking double sided Buisiness card with all my details phone number, name, email, license number.

Target Market(s)

construction industry

Industry/Entity Type

building

Contact Information for Business Card

Name Dale Whitcombe. Email Address Info@KPTBuilding.example.au mobile number 0452918730 licence number 871406D. web site

```html
<!DOCTYPE html>
<html lang="en">
<head>
<meta charset="utf-8">
<title>KPT Building And Maintenance – Business Card</title>
<link href="https://fonts.googleapis.com/css2?family=Exo+2:wght@400;600;700&display=swap" rel="stylesheet">
<style>
  :root {
    --page-bg: #e6e7e9;
    --card-white: #ffffff;
    --card-black: #070808;
    --pattern-dark: #141516;
    --brand-blue: #449bd6;
    --ink-grey: #4a4a4c;
    --ink-black: #1d1d1f;
    --shadow: rgba(0, 0, 0, 0.35);
  }
  * { box-sizing: border-box; margin: 0; padding: 0; }
  html, body {
    width: 1200px;
    height: 1200px;
    overflow: hidden;
    background: var(--page-bg);
    font-family: "Exo 2", sans-serif;
  }
  .canvas { position: relative; width: 1200px; height: 1200px; }
  .card {
    position: absolute;
    top: 480px;
    width: 420px;
    height: 240px;
    box-shadow: 8px 8px 10px var(--shadow);
  }
  .card-front { left: 158px; background: var(--card-white); }
  .card-back { left: 623px; background: var(--card-black); overflow: hidden; }

  .divider {
    position: absolute;
    left: 215px; top: 38px;
    width: 1px; height: 168px;
    background: var(--brand-blue);
  }
  .contact-block {
    position: absolute;
    right: 218px;
    top: 0;
    text-align: right;
  }
  .person-name {
    position: absolute;
    right: 0; top: 60px;
    white-space: nowrap;
    font-size: 19px;
    font-weight: 700;
    color: var(--brand-blue);
  }
  .contact-line {
    position: absolute;
    right: 0;
    display: flex;
    align-items: center;
    gap: 5px;
    white-space: nowrap;
    font-size: 12.5px;
    color: var(--ink-grey);
    letter-spacing: 0.2px;
  }
  .contact-line svg { width: 11px; height: 11px; flex: none; }
  .line-phone { top: 99px; }
  .line-email { top: 116px; }
  .line-web { top: 133px; }
  .licence {
    position: absolute;
    right: 0; top: 169px;
    white-space: nowrap;
    font-size: 12.5px;
    color: var(--ink-black);
  }
  .licence .licence-no { color: var(--ink-grey); }

  .wordmark {
    position: absolute;
    left: 230px; top: 58px;
    width: 167px;
    text-align: center;
    font-weight: 700;
    color: var(--ink-grey);
    line-height: 1;
  }
  .wordmark .wm-initials { display: block; font-size: 56px; letter-spacing: 1px; }
  .wordmark .wm-word { display: block; font-size: 27px; margin-top: 4px; letter-spacing: 0.5px; }
  .wordmark-rule {
    position: absolute;
    left: 230px; top: 183px;
    width: 167px; height: 1px;
    background: var(--brand-blue);
  }

  .back-texture {
    position: absolute; inset: 0;
    background: linear-gradient(180deg, var(--pattern-dark), var(--card-black));
  }
  .back-name {
    position: absolute;
    left: 37px; top: 176px;
    font-size: 31px;
    font-weight: 700;
    color: var(--card-white);
    letter-spacing: 0.5px;
    white-space: nowrap;
  }
</style>
</head>
<body>
<main class="canvas">
  <section class="card card-front" aria-label="Business card front">
    <div class="contact-block">
      <h1 class="person-name">Dale Whitcombe</h1>
      <p class="contact-line line-phone">045 291 8730
        <svg viewBox="0 0 12 12" aria-hidden="true"><path fill="var(--brand-blue)" d="M2.6 1l1.6 2.2-.9 1.1c.7 1.4 1.6 2.3 3 3l1.1-.9L11 8l-.4 1.7C10.4 10.5 9.7 11 9 11 4.6 10.6 1.4 7.4 1 3c0-.7.5-1.4 1.3-1.6z"/></svg>
      </p>
      <p class="contact-line line-email">Info@KPTBuilding.example.au
        <svg viewBox="0 0 12 12" aria-hidden="true"><rect x="0.5" y="2" width="11" height="8" fill="var(--brand-blue)"/><path d="M0.8 2.4L6 6.6l5.2-4.2" stroke="#fff" stroke-width="0.9" fill="none"/></svg>
      </p>
      <p class="contact-line line-web">www.KPTBuilding.example.au
        <svg viewBox="0 0 12 12" aria-hidden="true"><circle cx="6" cy="6" r="5.3" fill="var(--brand-blue)"/><path d="M1 6h10M6 .8v10.4M2 3.5h8M2 8.5h8" stroke="#fff" stroke-width="0.6"/><ellipse cx="6" cy="6" rx="2.3" ry="5.2" stroke="#fff" stroke-width="0.6" fill="none"/></svg>
      </p>
      <p class="licence">licence number <span class="licence-no">871406D</span></p>
    </div>
    <div class="divider"></div>
    <div class="wordmark">
      <span class="wm-initials">KPT</span>
      <span class="wm-word">BUILDING</span>
    </div>
    <div class="wordmark-rule"></div>
  </section>

  <section class="card card-back" aria-label="Business card back">
    <div class="back-texture" role="img" aria-label="Subtle dark chevron roof-line texture"></div>
    <p class="back-name">KPT BUILDING</p>
  </section>
</main>
</body>
</html>
```